Website redesign for a technology and engineering company

We'd like to redesign our website which can be found on quorvane.co.nz
!! Please find the designers brief as an uploaded file with all details in there!!
The main purpose for redesign is:
>change of services offered
>old website not very user friendly to maintain or update
Key requirements:
>visually appealing
>easy to navigate
>simple and easy to read
>responsive
>mobile device compatibility
>integrating best SEO practice
All the details are in the attached designer brief document.

```html
<!DOCTYPE html>
<html lang="en">
<head>
<meta charset="utf-8">
<title>Quorvane — Surveying &amp; Digital Mapping</title>
<link rel="stylesheet" href="https://fonts.googleapis.com/css2?family=Chakra+Petch:ital,wght@1,500;1,600&family=Urbanist:wght@400;500;600&display=swap">
<style>
:root{
  --black:#000;
  --panel:#161616;
  --panel-2:#1d1d1d;
  --line:#3a3a3a;
  --blue:#3d6ef0;
  --blue-soft:#5b86ff;
  --white:#fff;
  --muted:#cfcfcf;
  --head:"Chakra Petch", sans-serif;
  --body:"Urbanist", sans-serif;
}
*{margin:0;padding:0;box-sizing:border-box}
html,body{width:1200px;height:4666px;overflow:hidden;background:var(--black);color:var(--white);font-family:var(--body)}
.page{position:relative;width:1200px;height:4666px;overflow:hidden}
.abs{position:absolute}
.h-italic{font-family:var(--head);font-style:italic;font-weight:600}
.btn{position:absolute;display:flex;align-items:center;justify-content:center;background:var(--blue);color:var(--white);border-radius:20px;font-size:11px;letter-spacing:.3px;text-transform:uppercase}
.photo{position:absolute}
.arrow{position:absolute;width:28px;height:10px}

/* sidebar + hero */
.sidebar{left:0;top:0;width:112px;height:616px;background:var(--black)}
.brand{position:absolute;left:18px;top:18px;display:flex;align-items:center;gap:6px;font-size:18px;font-weight:600}
.brand .dot{width:10px;height:10px;border-radius:50%;background:var(--white)}
.scroll-track{position:absolute;left:55px;width:2px}
.scroll-label{position:absolute;left:46px;top:583px;transform:rotate(-90deg);transform-origin:left top;font-size:10px;letter-spacing:3px;color:var(--muted)}
.hero-photo{left:112px;top:0;width:1088px;height:616px;background:radial-gradient(ellipse at 40% 45%,#9a9a9a 0%,#6d6d6d 45%,#3f3f3f 100%)}
.nav{position:absolute;top:18px;right:114px;display:flex;align-items:center;gap:28px;font-size:11px}
.nav .cta{border:1px solid var(--white);border-radius:16px;padding:7px 16px;font-size:10px;text-transform:uppercase}
.hero-title{position:absolute;right:114px;top:124px;text-align:right;font-size:58px;line-height:68px}
.hero-text{position:absolute;right:114px;top:274px;width:520px;text-align:right;font-size:12px;line-height:17px}

.section-title{position:absolute;left:112px;font-size:34px}

/* services */
.svc-card{position:absolute;top:737px;width:315px;height:322px;background:var(--panel)}
.svc-card .photo{left:0;top:0;width:315px;height:266px}
.svc-card .label{position:absolute;left:12px;bottom:18px;font-size:15px}
.svc-card .arrow{right:18px;bottom:22px}
.svc-open{background:var(--panel-2)}
.svc-open .bar{position:absolute;left:0;top:0;width:315px;height:55px;background:var(--blue);display:flex;align-items:center;padding-left:12px;font-size:15px}
.svc-list{position:absolute;left:30px;top:80px;list-style:none;font-size:11px;line-height:25px}
.svc-list li{position:relative;padding-left:22px}
.svc-list li::before{content:"";position:absolute;left:0;top:10px;width:7px;height:7px;border-radius:50%;background:var(--blue)}

/* who */
.who-text{left:112px;top:1265px;width:370px;font-size:12px;line-height:18px}
.badge{position:absolute;left:563px;top:1292px;width:170px;height:147px;background:#1b1b1b;display:flex;flex-direction:column;align-items:center;justify-content:center;z-index:2;border:6px solid var(--black)}
.badge .num{font-family:var(--head);font-style:italic;font-weight:600;font-size:48px;color:var(--blue);line-height:1}
.badge .cap{font-size:14px;text-align:center;line-height:17px;margin-top:4px}

/* wordmark banners */
.wordmark{position:absolute;left:0;width:1200px;text-align:center;font-family:var(--body);font-weight:500;color:var(--white);letter-spacing:-6px;white-space:nowrap;line-height:1}

/* what we do */
.wwd-card{position:absolute;background:var(--panel)}
.wwd-card .label{position:absolute;font-size:15px}
.wwd-side .title{position:absolute;left:222px;top:30px;font-size:16px;line-height:18px}
.wwd-side .sub{position:absolute;left:222px;font-size:10px;line-height:12px;color:var(--muted)}

/* contact */
.form-panel{left:112px;top:3231px;width:487px;height:537px;background:var(--panel)}
.field{position:absolute;left:45px;width:391px;height:42px;border:1px solid #5a5a5a;border-radius:21px;padding:13px 26px;font-size:11px}
.field.area{height:153px;border-radius:14px}
.email-box{left:854px;top:3662px;width:232px;height:95px;background:#1b1b1b;border:6px solid var(--black)}

/* subscribe */
.subscribe{left:0;top:3832px;width:1200px;height:148px;background:var(--blue)}
.sub-input{position:absolute;left:592px;top:43px;width:329px;height:38px;border:1px solid var(--white);border-radius:19px;padding:11px 30px;font-size:11px}
.sub-btn{position:absolute;left:927px;top:43px;width:159px;height:38px;background:var(--white);color:var(--blue);border-radius:19px;font-size:11px;display:flex;align-items:center;justify-content:center;text-transform:uppercase}

/* footer */
.footer-col{position:absolute;top:4038px;font-size:11px;line-height:20px}
.footer-col h4{font-family:var(--head);font-style:italic;font-weight:600;font-size:14px;margin-bottom:2px}
</style>
</head>
<body>
<div class="page">

  <!-- Hero -->
  <div class="photo hero-photo" role="img" aria-label="Engineering parts, calipers and technical drawings on a desk"></div>
  <div class="abs sidebar">
    <div class="brand"><span class="dot"></span>Quorvane</div>
    <div class="scroll-track" style="top:225px;height:92px;background:var(--blue)"></div>
    <div class="scroll-track" style="top:325px;height:40px;background:#333"></div>
    <div class="scroll-track" style="top:375px;height:45px;background:#333"></div>
    <div class="scroll-label">SCROLL DOWN</div>
  </div>
  <nav class="nav">
    <span>What We Do</span><span>About</span><span>Services</span><span>Projects</span><span>Contact</span>
    <svg width="11" height="11" viewBox="0 0 12 12" fill="none" stroke="#fff" stroke-width="1.4"><circle cx="5" cy="5" r="4"/><path d="M8 8l3 3"/></svg>
    <span class="cta">Get In Touch</span>
  </nav>
  <h1 class="hero-title h-italic">Best Surveying &amp; Digital<br>Mapping Service</h1>
  <p class="hero-text">Quorvane was born out of our team having experienced difficult field operations in rugged terrain, often involving helicopters, boats and 4WD vehicles.</p>
  <div class="btn" style="left:939px;top:324px;width:141px;height:36px;text-transform:none;font-size:12px">LEARN MORE</div>

  <!-- Services -->
  <h2 class="section-title h-italic" style="top:670px">Services We Offered</h2>
  <div class="svc-card" style="left:112px">
    <div class="photo" role="img" aria-label="Survey instrument on a tripod in a green field" style="background:linear-gradient(180deg,#c9ccd0 0%,#a7adb1 35%,#5f7a3e 60%,#3e5a2a 100%)"></div>
    <div class="label h-italic">Fildwork Solutions</div>
    <svg class="arrow" viewBox="0 0 28 10" fill="none" stroke="#3d6ef0" stroke-width="1.3"><path d="M0 5h26M22 1l4 4-4 4"/></svg>
  </div>
  <div class="svc-card svc-open" style="left:442px">
    <div class="bar h-italic">Positioning And Monitoring
      <svg style="position:absolute;right:22px;top:16px" width="10" height="24" viewBox="0 0 10 24" fill="none" stroke="#fff" stroke-width="1.3"><path d="M5 0v22M1 18l4 4 4-4"/></svg>
    </div>
    <ul class="svc-list">
      <li>Real-Time Kinematic (RTK) Solutions</li>
      <li>Custom GNSS Base stations</li>
      <li>NTRIP service</li>
      <li>Tailored Monitoring Solutions</li>
      <li>Environmental Monitoring</li>
      <li>Robust communication Systems</li>
      <li>Internet of Things (IoT) Integration</li>
      <li>Solar powered systems</li>
      <li>Smart Sensor Networks</li>
    </ul>
  </div>
  <div class="svc-card" style="left:771px">
    <div class="photo" role="img" aria-label="Monitoring station hut in snowy fog" style="background:linear-gradient(180deg,#7f8a98 0%,#9aa4b0 50%,#c9cfd6 100%)"></div>
    <div class="label h-italic">Design And Prototyping</div>
    <svg class="arrow" viewBox="0 0 28 10" fill="none" stroke="#3d6ef0" stroke-width="1.3"><path d="M0 5h26M22 1l4 4-4 4"/></svg>
  </div>

  <!-- Who we are -->
  <h2 class="section-title h-italic" style="top:1210px">Who We Are</h2>
  <p class="abs who-text">Welcome to Quorvane, your reliable partner in delivering innovative solutions. Our team of skilled professionals is committed to excellence, ensuring every project is handled with precision, efficiency, and integrity. We solve problems in the field, build robust infrastructure, and deliver accurate data to our clients. Let us help you achieve your goals with our tailored, sustainable solutions and exceptional service.</p>
  <div class="btn" style="left:112px;top:1430px;width:132px;height:38px">Contact Us</div>
  <div class="photo" role="img" aria-label="Solar-powered monitoring station on a rocky mountain top under blue sky" style="left:648px;top:1175px;width:438px;height:393px;background:linear-gradient(180deg,#2f6fc4 0%,#5b93d6 35%,#8a8f94 60%,#5f6366 100%)"></div>
  <div class="badge"><div class="num">15+</div><div class="cap">Years of<br>Experience</div></div>

  <!-- Wordmark banner -->
  <div class="photo" role="img" aria-label="Misty snow-capped mountain range" style="left:0;top:1557px;width:1200px;height:459px;background:linear-gradient(180deg,#000 0%,#8c8c8c 35%,#d7d7d7 48%,#5a5a5a 68%,#2e2e2e 100%)"></div>
  <div class="wordmark" style="top:1630px;font-size:290px">Quorvane</div>

  <!-- What we do -->
  <h2 class="section-title h-italic" style="top:2082px">What We Do</h2>
  <div class="wwd-card" style="left:112px;top:2148px;width:559px;height:323px">
    <div class="photo" role="img" aria-label="Survey drone in flight against a sunset sky" style="left:0;top:0;width:559px;height:265px;background:linear-gradient(180deg,#7e8ea6 0%,#c6cbd4 55%,#e6d3bf 100%)"></div>
    <div class="label h-italic" style="left:16px;top:282px">UAV &amp; Survey Services</div>
    <svg class="arrow" style="right:32px;top:290px" viewBox="0 0 28 10" fill="none" stroke="#3d6ef0" stroke-width="1.3"><path d="M0 5h26M22 1l4 4-4 4"/></svg>
  </div>
  <div class="wwd-card wwd-side" style="left:690px;top:2148px;width:396px;height:160px">
    <div class="photo" role="img" aria-label="Equipment cabinet and antenna among trees" style="left:0;top:0;width:208px;height:160px;background:linear-gradient(180deg,#5e8a3e 0%,#3d5e2e 55%,#c9cbc7 100%)"></div>
    <div class="title h-italic">Technical Field<br>Operations</div>
    <div class="sub" style="top:75px">Install &amp; Maintenance of<br>Remote Infrastructure</div>
    <svg class="arrow" style="left:236px;top:128px" viewBox="0 0 28 10" fill="none" stroke="#3d6ef0" stroke-width="1.3"><path d="M0 5h26M22 1l4 4-4 4"/></svg>
  </div>
  <div class="wwd-card wwd-side" style="left:690px;top:2320px;width:396px;height:151px">
    <div class="photo" role="img" aria-label="Electronics control board with breakers and wiring" style="left:0;top:0;width:208px;height:151px;background:linear-gradient(135deg,#2b2b2b 0%,#8a6a45 50%,#3a3a3a 100%)"></div>
    <div class="title h-italic" style="top:24px">Design &amp;<br>Prototyping</div>
    <div class="sub" style="top:69px">Drawings &amp; Models For<br>Manufacturing</div>
    <svg class="arrow" style="left:236px;top:122px" viewBox="0 0 28 10" fill="none" stroke="#3d6ef0" stroke-width="1.3"><path d="M0 5h26M22 1l4 4-4 4"/></svg>
  </div>

  <!-- Project cases -->
  <div class="abs" style="left:0;top:2561px;width:1200px;height:610px;background:linear-gradient(180deg,#151515 0%,#0a0a0a 100%)"></div>
  <h2 class="section-title h-italic" style="top:2616px">Project Cases</h2>
  <p class="abs" style="left:112px;top:2665px;font-size:12px">Check out some projects we have been working on</p>
  <div class="btn" style="left:939px;top:2628px;width:147px;height:36px">Discover More</div>
  <div class="photo" role="img" aria-label="Rusted railway tracks beside a bridge" style="left:0;top:2704px;width:292px;height:373px;background:linear-gradient(180deg,#a7b4c2 0%,#6b5a4b 45%,#7a4b2e 100%)"></div>
  <div class="photo" role="img" aria-label="Equipment cases in a red inflatable boat near rocky islands" style="left:302px;top:2704px;width:292px;height:373px;background:linear-gradient(180deg,#8fb0d6 0%,#2c5a86 40%,#a32a22 75%,#1c1c1c 100%)"></div>
  <div class="photo" role="img" aria-label="Aerial view of a mast beside dark water" style="left:604px;top:2704px;width:292px;height:373px;background:linear-gradient(90deg,#3b4a3c 0%,#6d7566 50%,#a9a69b 100%)"></div>
  <div class="photo" role="img" aria-label="Hilltop station overlooking a bay and islands" style="left:906px;top:2704px;width:294px;height:373px;background:linear-gradient(180deg,#9fb3c9 0%,#6f8aa4 45%,#8a7c55 75%,#5d5436 100%)"></div>

  <!-- Contact -->
  <div class="abs" style="left:599px;top:3168px;width:601px;height:600px;background:var(--black)"></div>
  <div class="abs form-panel">
    <h2 class="abs h-italic" style="left:45px;top:42px;font-size:34px">Send Us a Message</h2>
    <div class="field" style="top:99px">Name</div>
    <div class="field" style="top:159px">Email</div>
    <div class="field" style="top:219px">Subject</div>
    <div class="field area" style="top:279px">Message (Optional)</div>
    <div class="btn" style="left:45px;top:454px;width:160px;height:38px">Send Message</div>
  </div>
  <div class="photo" role="img" aria-label="Engineers in hard hats reviewing building plans at a table" style="left:599px;top:3231px;width:487px;height:416px;background:linear-gradient(135deg,#d9d4c8 0%,#e6e2d8 40%,#c9a14a 70%,#4f6f99 100%)"></div>
  <div class="abs email-box">
    <svg style="position:absolute;left:14px;top:19px" width="46" height="46" viewBox="0 0 46 46" fill="none"><circle cx="23" cy="23" r="22" stroke="#3d6ef0" stroke-width="1.2"/><rect x="14" y="16" width="18" height="13" rx="1.5" fill="#3d6ef0"/><path d="M14 17l9 7 9-7" stroke="#1b1b1b" stroke-width="1.3"/></svg>
    <div class="abs h-italic" style="left:94px;top:22px;font-size:16px">Email us:</div>
    <div class="abs" style="left:94px;top:48px;font-size:11px;color:var(--blue-soft)">hi@quorvane.nz</div>
  </div>

  <!-- Subscribe -->
  <div class="abs subscribe">
    <h2 class="abs h-italic" style="left:112px;top:52px;font-size:34px">Subscribe To Our Email</h2>
    <div class="sub-input">Enter Your Email Here</div>
    <div class="sub-btn">Subscribe</div>
    <p class="abs" style="left:608px;top:99px;font-size:11px">By subscribing, you agree with our privacy policy and our terms of service.</p>
  </div>

  <!-- Footer -->
  <div class="photo" role="img" aria-label="Snowy mountain range reflected in a still lake" style="left:0;top:4160px;width:1200px;height:506px;background:linear-gradient(180deg,#000 0%,#6d7f95 25%,#b9c4cf 45%,#3d4f63 65%,#7e93ab 80%,#2a3442 100%)"></div>
  <div class="wordmark" style="top:4150px;font-size:290px">Quorvane</div>
  <div class="abs" style="left:112px;top:4052px;display:flex;align-items:center;gap:8px;font-size:26px;font-weight:600"><span style="width:14px;height:14px;border-radius:50%;background:#fff;display:inline-block"></span>Quorvane</div>
  <div class="abs" style="left:112px;top:4112px;display:flex;align-items:center;gap:10px;font-size:11px">Follow Us:
    <span style="width:42px;height:42px;border-radius:50%;border:1.5px solid var(--blue);display:inline-block"></span>
  </div>
  <div class="footer-col" style="left:416px"><h4>QUICK LINKS</h4>What We Do<br>About<br>Services<br>Projects<br>Contact</div>
  <div class="footer-col" style="left:634px"><h4>WHAT WE DO</h4>UAV &amp; Survey Services<br>Technical Field Operations<br>Design &amp; Prototyping</div>
  <div class="footer-col" style="left:907px"><h4>SERVICES</h4>Fildwork Solutions<br>Positioning And Monitoring<br>Design And Prototyping</div>
  <p class="abs" style="left:280px;top:4500px;width:640px;text-align:center;font-size:12px;line-height:17px">We are field operations experts with backgrounds in surveying, geoscience, and technical field work. Our purpose is to solve problems in the field, build robust infrastructure and deliver accurate data to our clients.</p>
  <div class="abs" style="left:112px;top:4615px;width:974px;height:1px;background:rgba(255,255,255,.5)"></div>
  <div class="abs" style="left:0;top:4636px;width:1200px;display:flex;justify-content:center;gap:30px;font-size:10px">
    <span>Copyright © Quorvane 2024. All Rights Reserved.</span><span>Privacy Policy</span><span>Disclaimer</span>
  </div>

</div>
</body>
</html>
```